FinTech company looking to revamp and expand client-facing interface for our financial models

Halvern Ledgerworks currently has a very simple website that allows clients to interact with our financial models. We are looking to completely redesign the current site and add several extra pages to provide extra functionality. We want the design to have a modern, slick feel, that will work on both a desktop or a tablet. It should be straightforward for clients to move between different pages at any time, and clear from the layout how to interact with the more advanced features. We have included screenshots of existing pages in the attached design brief, as well as sketches of the functionality required by the new pages, but can't provide a direct link to the current site.
Target Market(s)
Professional investors that will be paying to access the interface
Industry/Entity Type
Finance
Number of Pages Required
4 page
Colors
Designer to choose colors to be used in the design.
Look and feel
Each slider illustrates characteristics of the customer's brand and the style your logo design should communicate.

```html
<!DOCTYPE html>
<html lang="en">
<head>
<meta charset="utf-8">
<title>Halvern Ledgerworks – Models</title>
<link href="https://fonts.googleapis.com/css2?family=Roboto:wght@400;500;700&display=swap" rel="stylesheet">
<style>
:root{
  --page:#dde3ef;
  --screen:#f4f6fb;
  --card:#ffffff;
  --brand:#3340ff;
  --ink:#2a2d3a;
  --muted:#8a90a6;
  --nav:#a9b0c8;
  --line:#e6e8ef;
  --purple:#a66be8;
  --teal:#2fcca5;
  --coral:#ec6a4e;
  --series-a:#8f86f2;
  --series-b:#c08ae6;
}
*{box-sizing:border-box;margin:0;padding:0}
html,body{width:1200px;height:1200px;overflow:hidden;background:var(--page);font-family:'Roboto',sans-serif;color:var(--ink)}
.screen{position:absolute;left:333px;width:905px;background:var(--screen);transform:scale(.621);transform-origin:0 0;box-shadow:0 4px 18px rgba(40,50,90,.12)}
.screen--models{top:37px;height:631px}
.screen--details{top:463px;height:1110px}
.abs{position:absolute}
.brand{left:32px;top:30px;font-size:24px;font-weight:700;color:var(--brand);letter-spacing:.5px}
.nav{left:18px;top:72px;width:100px}
.nav-item{display:flex;align-items:center;height:37.3px;font-size:9px;color:var(--nav);font-weight:500}
.nav-item svg{width:20px;height:20px;margin-right:19px;fill:var(--nav)}
.nav-item--active{color:var(--ink);font-weight:700}
.nav-item--active svg{fill:var(--ink)}
.topbar{left:132px;top:20px;width:584px;height:42px;background:var(--brand);border-radius:3px;color:#fff;display:flex;align-items:center;padding:0 19px;font-size:9px}
.topbar .title{font-weight:700;letter-spacing:.3px;flex:1;display:flex;align-items:center;gap:14px}
.topbar .select{display:flex;align-items:center;gap:10px;margin-left:22px}
.caret{width:0;height:0;border-left:4px solid transparent;border-right:4px solid transparent;border-top:4px solid #fff}
.card{background:var(--card);border-radius:3px;box-shadow:0 1px 4px rgba(40,50,90,.05)}
.main{left:132px;top:77px;width:584px}
.field{position:absolute;top:19px;height:30px;width:260px;border:1px solid #d6d9e3;border-radius:3px;font-size:10px;padding:8px 11px}
.field label{position:absolute;top:-5px;left:7px;background:#fff;padding:0 3px;font-size:6.5px;color:var(--muted)}
.field--active{border:1.5px solid var(--brand)}
.field--active label{color:var(--brand)}
table{border-collapse:collapse;font-size:9.5px;table-layout:fixed}
th{font-weight:400;color:var(--muted);height:34px;border-bottom:1px solid var(--line)}
td{height:39.5px;border-bottom:1px solid var(--line);text-align:center;line-height:1.2}
.data{position:absolute;left:20px;width:544px}
.pager{position:absolute;right:20px;display:flex;align-items:center;gap:14px;font-size:9px;color:var(--muted)}
.pager .caret{border-top-color:var(--muted)}
.pager .rows{display:flex;align-items:center;gap:12px;margin-right:12px}
.chev{width:6px;height:6px;border-left:1.4px solid var(--ink);border-bottom:1.4px solid var(--ink)}
.chev--l{transform:rotate(45deg)}
.chev--r{transform:rotate(-135deg)}
.section-title{position:absolute;left:0;width:100%;text-align:center;font-size:12px;font-weight:500}
.side{left:735px;width:150px}
.card-head{height:41px;border-bottom:1px solid var(--line);display:flex;align-items:center;justify-content:space-between;padding:0 12px 0 19px;font-size:8px;font-weight:700}
.dots{display:flex;gap:2.5px}
.dots i{width:2.5px;height:2.5px;border-radius:50%;background:var(--muted)}
.avatar{position:absolute;left:35px;top:53px;width:80px;height:80px;border-radius:50%;background:radial-gradient(circle at 50% 40%,#8a6a50,#3b2a22)}
.name{position:absolute;top:145px;width:100%;text-align:center;font-size:10.5px;font-weight:500}
.email{position:absolute;top:159px;width:100%;text-align:center;font-size:8px;color:var(--nav)}
.volume{display:flex;align-items:center;gap:9px;padding:13px 12px;font-size:10.5px;font-weight:700;color:var(--brand)}
.plus{width:18px;height:18px;border-radius:50%;background:#e6e7ff;position:relative}
.plus::before,.plus::after{content:"";position:absolute;left:50%;top:50%;background:var(--brand);transform:translate(-50%,-50%)}
.plus::before{width:8px;height:1.2px}.plus::after{width:1.2px;height:8px}
.legend{position:absolute;top:175px;left:0;width:100%;display:flex;justify-content:center;gap:13px;font-size:6.5px;color:var(--muted)}
.legend span{display:flex;align-items:center;gap:4px}
.legend i{width:6px;height:6px;border-radius:50%}
.cta{height:39px;background:var(--coral);border-radius:3px;color:#fff;font-size:7.5px;font-weight:700;display:flex;align-items:center;justify-content:space-between;padding:0 12px 0 19px}
.actions{display:flex;align-items:center;font-size:7.5px;color:var(--nav);font-weight:500}
.actions .btn{width:25px;height:25px;border-radius:50%;border:1px solid #c9cedd;margin-left:12px;display:flex;align-items:center;justify-content:center}
.actions .btn svg{width:11px;height:11px;fill:var(--nav)}
.chart{position:absolute;left:20px}
.chart text{font-family:'Roboto',sans-serif;fill:var(--ink)}
</style>
</head>
<body>

<!-- Models screen -->
<section class="screen screen--models">
  <div class="abs brand">Halvern</div>
  <nav class="abs nav">
    <div class="nav-item nav-item--active"><svg viewBox="0 0 20 20"><path d="M10 2 2 9v9h6v-5h4v5h6V9z"/></svg>Models</div>
    <div class="nav-item"><svg viewBox="0 0 20 20"><rect x="5" y="2" width="10" height="16" rx="5"/></svg>Sensitivities</div>
    <div class="nav-item"><svg viewBox="0 0 20 20"><path d="M10 1l2.6 6 6.4.5-4.9 4.2 1.5 6.3L10 14.7 4.4 18l1.5-6.3L1 7.5 7.4 7z"/></svg>Favourites</div>
    <div class="nav-item"><svg viewBox="0 0 20 20"><rect x="1" y="5" width="3" height="12"/><rect x="7" y="9" width="12" height="8" rx="1"/><rect x="13" y="3" width="3" height="7"/></svg>Menuitem</div>
    <div class="nav-item"><svg viewBox="0 0 20 20"><circle cx="10" cy="10" r="6.5" fill="none" stroke="#a9b0c8" stroke-width="5" stroke-dasharray="3 2.1"/><circle cx="10" cy="10" r="5"/><circle cx="10" cy="10" r="2" fill="#f4f6fb"/></svg>Settings</div>
  </nav>

  <header class="abs topbar">
    <div class="title">MODELS</div>
    <div class="select">Equities <i class="caret"></i></div>
    <div class="select">Select model type <i class="caret"></i></div>
  </header>

  <div class="abs card main" style="height:537px">
    <div class="field" style="left:20px"><label>Quality</label>Threshold</div>
    <div class="field field--active" style="left:302px"><label>Abs. Star</label>10</div>
    <table class="data" style="top:61px">
      <colgroup><col style="width:55px"><col style="width:70px"><col style="width:72px"><col style="width:69px"><col style="width:71px"><col style="width:71px"><col style="width:67px"><col style="width:69px"></colgroup>
      <thead><tr><th></th><th>Sector</th><th>Time</th><th>Quality</th><th>Star 1</th><th>Star 2</th><th>Star 3</th><th>Star 4</th></tr></thead>
      <tbody>
        <tr><td>1</td><td>Materials</td><td>29-07-2013<br>12:15:00:00</td><td>30.2288</td><td>2.01574</td><td>23.305</td><td>-0.129468</td><td>172.616</td></tr>
        <tr><td>2</td><td>Industrials</td><td>29-07-2013<br>12:15:00:00</td><td>40.2200</td><td>3.54712</td><td>21.032</td><td>0.00475</td><td>112.056</td></tr>
        <tr><td>3</td><td>Consumer<br>Discretionary</td><td>29-07-2013<br>12:15:00:00</td><td>20.2288</td><td>2.01574</td><td>23.305</td><td>1.02356</td><td>222.021</td></tr>
        <tr><td>4</td><td>Information<br>technology</td><td>29-07-2013<br>12:15:00:00</td><td>10.5566</td><td>1.25680</td><td>20.000</td><td>-0.129468</td><td>172.616</td></tr>
        <tr><td>5</td><td>Materials</td><td>29-07-2013<br>12:15:00:00</td><td>80.0000</td><td>2.01574</td><td>12.225</td><td>-0.129468</td><td>172.616</td></tr>
        <tr><td>6</td><td>Information<br>technology</td><td>29-07-2013<br>12:15:00:00</td><td>12.0000</td><td>2.01574</td><td>23.305</td><td>-0.129468</td><td>172.616</td></tr>
        <tr><td>7</td><td>Materials</td><td>29-07-2013<br>12:15:00:00</td><td>30.2288</td><td>2.01574</td><td>23.305</td><td>-0.129468</td><td>172.616</td></tr>
        <tr><td>8</td><td>Materials</td><td>29-07-2013<br>12:15:00:00</td><td>30.2288</td><td>2.01574</td><td>23.305</td><td>-0.129468</td><td>172.616</td></tr>
        <tr><td>9</td><td>Materials</td><td>29-07-2013<br>12:15:00:00</td><td>30.2288</td><td>2.01574</td><td>23.305</td><td>-0.129468</td><td>172.616</td></tr>
        <tr><td>10</td><td>Materials</td><td>29-07-2013<br>12:15:00:00</td><td>30.2288</td><td>2.01574</td><td>23.305</td><td>-0.129468</td><td>172.616</td></tr>
      </tbody>
    </table>
    <div class="pager" style="top:507px"><span>Rows per page</span><span class="rows">10 <i class="caret"></i></span><span>1-10 out of 100</span><i class="chev chev--l"></i><i class="chev chev--r"></i></div>
  </div>

  <aside class="abs side" style="top:20px">
    <div class="card" style="position:relative;height:182px">
      <div class="card-head">PROFILE <svg width="9" height="10" viewBox="0 0 9 10" fill="#a9b0c8"><path d="M4.5 0a3 3 0 0 1 3 3v3l1.5 2H0l1.5-2V3a3 3 0 0 1 3-3zM3.3 9h2.4a1.2 1.2 0 0 1-2.4 0z"/></svg></div>
      <div class="avatar" role="img" aria-label="Profile portrait photo"></div>
      <div class="name">Rowan Pike</div>
      <div class="email">rowanpike@ledgerworks.example</div>
    </div>
    <div class="card" style="margin-top:18px;height:87px">
      <div class="card-head">TODAYS VOLUME <span class="dots"><i></i><i></i><i></i></span></div>
      <div class="volume"><span class="plus"></span>$1840.95 (10.64%)</div>
    </div>
    <div class="card" style="position:relative;margin-top:18px;height:195px">
      <div class="card-head">CARD TITLE <span class="dots"><i></i><i></i><i></i></span></div>
      <svg class="abs" style="left:25px;top:52px" width="100" height="100" viewBox="0 0 100 100">
        <circle cx="50" cy="50" r="44" fill="none" stroke="var(--teal)" stroke-width="13" stroke-dasharray="31 246" transform="rotate(-122 50 50)"/>
        <circle cx="50" cy="50" r="44" fill="none" stroke="var(--purple)" stroke-width="13" stroke-dasharray="81 196" transform="rotate(-70 50 50)"/>
        <circle cx="50" cy="50" r="44" fill="none" stroke="var(--brand)" stroke-width="13" stroke-dasharray="131 146" transform="rotate(42 50 50)"/>
        <text x="51" y="51" text-anchor="middle" font-family="Roboto,sans-serif" font-size="13" font-weight="500" fill="#2a2d3a">23%</text>
        <text x="50" y="62" text-anchor="middle" font-family="Roboto,sans-serif" font-size="8" font-weight="500" fill="#2a2d3a">item 3</text>
      </svg>
      <div class="legend"><span><i style="background:var(--brand)"></i>Item 1</span><span><i style="background:var(--purple)"></i>Item 2</span><span><i style="background:var(--teal)"></i>Item 3</span></div>
    </div>
    <div class="cta" style="margin-top:17px">SOME BUTTON <svg width="12" height="10" viewBox="0 0 12 10" fill="none" stroke="#fff" stroke-width="1.3"><path d="M0 5h11M7 1l4 4-4 4"/></svg></div>
    <div class="actions" style="margin-top:14px">Actions
      <span class="btn" style="margin-left:22px"><svg viewBox="0 0 12 12"><path d="M1 11l.6-3L8.5 1.1l2.4 2.4L4 10.4z"/></svg></span>
      <span class="btn"><svg viewBox="0 0 12 12"><rect x="2.5" y="3" width="7" height="8.5" rx="1"/><rect x="1.5" y="1.3" width="9" height="1.2"/></svg></span>
      <span class="btn"><svg viewBox="0 0 12 12"><circle cx="2.5" cy="6" r="1.6"/><circle cx="9.5" cy="2.5" r="1.6"/><circle cx="9.5" cy="9.5" r="1.6"/><path d="M2.5 6 9.5 2.5M2.5 6l7 3.5" stroke="#a9b0c8" stroke-width="1"/></svg></span>
    </div>
  </aside>
</section>

<!-- Model details screen -->
<section class="screen screen--details">
  <div class="abs brand">Halvern</div>
  <nav class="abs nav">
    <div class="nav-item nav-item--active"><svg viewBox="0 0 20 20"><path d="M10 2 2 9v9h6v-5h4v5h6V9z"/></svg>Models</div>
    <div class="nav-item"><svg viewBox="0 0 20 20"><rect x="5" y="2" width="10" height="16" rx="5"/></svg>Sensitivities</div>
    <div class="nav-item"><svg viewBox="0 0 20 20"><path d="M10 1l2.6 6 6.4.5-4.9 4.2 1.5 6.3L10 14.7 4.4 18l1.5-6.3L1 7.5 7.4 7z"/></svg>Favourites</div>
    <div class="nav-item"><svg viewBox="0 0 20 20"><rect x="1" y="5" width="3" height="12"/><rect x="7" y="9" width="12" height="8" rx="1"/><rect x="13" y="3" width="3" height="7"/></svg>Menuitem</div>
    <div class="nav-item"><svg viewBox="0 0 20 20"><circle cx="10" cy="10" r="6.5" fill="none" stroke="#a9b0c8" stroke-width="5" stroke-dasharray="3 2.1"/><circle cx="10" cy="10" r="5"/><circle cx="10" cy="10" r="2" fill="#f4f6fb"/></svg>Settings</div>
  </nav>

  <header class="abs topbar">
    <div class="title"><svg width="12" height="10" viewBox="0 0 12 10" fill="none" stroke="#fff" stroke-width="1.3"><path d="M12 5H1M5 1 1 5l4 4"/></svg>MODEL DETAILS</div>
    <div class="select">Equities <i class="caret"></i></div>
    <div class="select">250D <i class="caret"></i></div>
  </header>

  <div class="abs card main" style="top:78px;height:1007px">
    <div class="section-title" style="top:14px">Number of selected factors</div>
    <table class="data" style="top:38px">
      <colgroup><col style="width:55px"><col style="width:150px"><col style="width:140px"><col style="width:140px"><col style="width:59px"></colgroup>
      <thead><tr><th></th><th style="text-align:left">Star 1</th><th>Star 2</th><th>Star 3</th><th>Star 4</th></tr></thead>
      <tbody>
        <tr><td>1</td><td style="text-align:left">2.01574</td><td>23.305</td><td>-0.129468</td><td>172.616</td></tr>
        <tr><td>2</td><td style="text-align:left">3.54712</td><td>21.032</td><td>0.00475</td><td>112.056</td></tr>
        <tr><td>3</td><td style="text-align:left">2.01574</td><td>23.305</td><td>1.02356</td><td>222.021</td></tr>
        <tr><td>4</td><td style="text-align:left">1.25680</td><td>20.000</td><td>-0.129468</td><td>172.616</td></tr>
        <tr><td>5</td><td style="text-align:left">2.01574</td><td>12.225</td><td>-0.129468</td><td>172.616</td></tr>
      </tbody>
    </table>
    <div class="pager" style="top:278px"><span>Rows per page</span><span class="rows">5 <i class="caret"></i></span><span>1-10 out of 100</span><i class="chev chev--l"></i><i class="chev chev--r"></i></div>

    <div class="section-title" style="top:312px">Unselected factors</div>
    <table class="data" style="top:336px">
      <colgroup><col style="width:55px"><col style="width:150px"><col style="width:140px"><col style="width:140px"><col style="width:59px"></colgroup>
      <thead><tr><th></th><th style="text-align:left;padding-left:2px">Factor</th><th>Factor</th><th>Factor</th><th>Factor</th></tr></thead>
      <tbody>
        <tr><td>1</td><td style="text-align:left;padding-left:2px">Factor</td><td>Factor</td><td>Factor</td><td>Factor</td></tr>
        <tr><td>2</td><td style="text-align:left;padding-left:2px">Factor</td><td>Factor</td><td>Factor</td><td>Factor</td></tr>
      </tbody>
    </table>
    <div class="pager" style="top:462px"><span>Rows per page</span><span class="rows">2 <i class="caret"></i></span><span>2-2 out of 2</span><i class="chev chev--l"></i><i class="chev chev--r"></i></div>

    <div class="section-title" style="top:506px">Graph 1</div>
    <svg class="chart" style="top:530px" width="544" height="200" viewBox="0 0 544 200">
      <g stroke="#eef0f5" stroke-width="1">
        <line x1="17" y1="8" x2="527" y2="8"/><line x1="17" y1="31" x2="527" y2="31"/><line x1="17" y1="54" x2="527" y2="54"/><line x1="17" y1="77" x2="527" y2="77"/><line x1="17" y1="101" x2="527" y2="101"/><line x1="17" y1="124" x2="527" y2="124"/><line x1="17" y1="147" x2="527" y2="147"/><line x1="17" y1="173" x2="527" y2="173"/>
      </g>
      <g font-size="6" text-anchor="end">
        <text x="11" y="10">50</text><text x="11" y="33">45</text><text x="11" y="56">40</text><text x="11" y="79">35</text><text x="11" y="103">30</text><text x="11" y="126">25</text><text x="11" y="149">20</text><text x="11" y="175">10</text>
      </g>
      <g font-size="6" text-anchor="middle">
        <text x="55" y="192">August 18</text><text x="113" y="192">August 18</text><text x="171" y="192">August 18</text><text x="229" y="192">August 18</text><text x="287" y="192">August 18</text><text x="345" y="192">August 18</text><text x="403" y="192">August 18</text><text x="461" y="192">August 18</text><text x="519" y="192">August 18</text>
      </g>
      <polyline fill="none" stroke="var(--series-a)" stroke-width="1" points="20,12 29,5 37,18 45,8 53,22 61,14 69,30 77,26 85,20 93,35 101,28 109,22 117,15 125,25 133,10 141,26 150,32 163,17 171,48 180,58 188,72 196,68 204,80 212,75 222,95 230,88 240,100 248,92 256,110 264,105 272,115 282,120 290,108 300,125 308,118 318,135 326,128 336,140 346,132 356,150 366,138 376,145 388,160 398,150 410,148 420,165 432,155 444,160 456,150 468,163 480,148 492,158 504,160 515,165 525,170"/>
      <polyline fill="none" stroke="var(--series-b)" stroke-width="1" points="20,10 28,20 36,8 44,40 52,60 60,70 68,55 76,75 84,62 92,80 100,88 108,58 116,20 124,18 131,45 138,100 146,60 156,35 164,17 172,46 180,65 190,85 198,80 208,100 216,95 226,112 236,105 246,125 256,130 266,140 276,120 286,135 296,145 306,130 316,150 326,148 336,155 346,140 356,150 366,128 376,150 386,155 396,150 408,138 420,115 432,140 444,155 456,150 468,160 480,150 494,168 506,160 516,172 525,172"/>
      <line x1="17" y1="17" x2="163" y2="17" stroke="#b8bccb" stroke-width=".8" stroke-dasharray="2 2"/>
      <line x1="163" y1="17" x2="163" y2="173" stroke="#b8bccb" stroke-width=".8" stroke-dasharray="2 2"/>
      <circle cx="163" cy="17" r="3" fill="var(--purple)"/>
      <text x="169" y="19" font-size="5">Something over here...</text>
      <rect x="479" y="10" width="46" height="42" fill="#fff" stroke="#eef0f5"/>
      <text x="502" y="20" font-size="5.5" font-weight="700" text-anchor="middle">Title</text>
      <circle cx="490" cy="31" r="2.5" fill="var(--series-a)"/><text x="498" y="33" font-size="4.5">Item 1</text>
      <circle cx="490" cy="43" r="2.5" fill="var(--series-b)"/><text x="498" y="45" font-size="4.5">Item 2</text>
    </svg>

    <div class="section-title" style="top:758px">Graph 2</div>
    <svg class="chart" style="top:782px" width="544" height="200" viewBox="0 0 544 200">
      <g stroke="#eef0f5" stroke-width="1">
        <line x1="17" y1="8" x2="527" y2="8"/><line x1="17" y1="31" x2="527" y2="31"/><line x1="17" y1="54" x2="527" y2="54"/><line x1="17" y1="77" x2="527" y2="77"/><line x1="17" y1="101" x2="527" y2="101"/><line x1="17" y1="124" x2="527" y2="124"/><line x1="17" y1="147" x2="527" y2="147"/><line x1="17" y1="173" x2="527" y2="173"/>
      </g>
      <g font-size="6" text-anchor="end">
        <text x="11" y="10">50</text><text x="11" y="33">45</text><text x="11" y="56">40</text><text x="11" y="79">35</text><text x="11" y="103">30</text><text x="11" y="126">25</text><text x="11" y="149">20</text><text x="11" y="175">10</text>
      </g>
      <g font-size="6" text-anchor="middle">
        <text x="55" y="192">August 18</text><text x="113" y="192">August 18</text><text x="171" y="192">August 18</text><text x="229" y="192">August 18</text><text x="287" y="192">August 18</text><text x="345" y="192">August 18</text><text x="403" y="192">August 18</text><text x="461" y="192">August 18</text><text x="519" y="192">August 18</text>
      </g>
      <g fill="var(--series-b)">
        <circle cx="24" cy="14" r="2.5"/><circle cx="30" cy="18" r="2.5"/><circle cx="36" cy="15" r="2.5"/><circle cx="42" cy="17" r="2.5"/><circle cx="48" cy="15" r="2.5"/><circle cx="54" cy="19" r="2.5"/><circle cx="66" cy="14" r="2.5"/>
        <circle cx="22" cy="25" r="2.5"/><circle cx="28" cy="29" r="2.5"/><circle cx="34" cy="24" r="2.5"/><circle cx="40" cy="27" r="2.5"/><circle cx="46" cy="22" r="2.5"/><circle cx="52" cy="28" r="2.5"/><circle cx="58" cy="25" r="2.5"/><circle cx="72" cy="30" r="2.5"/><circle cx="88" cy="24" r="2.5"/>
        <circle cx="26" cy="36" r="2.5"/><circle cx="36" cy="34" r="2.5"/><circle cx="44" cy="38" r="2.5"/><circle cx="50" cy="35" r="2.5"/><circle cx="60" cy="32" r="2.5"/><circle cx="22" cy="42" r="2.5"/><circle cx="38" cy="41" r="2.5"/><circle cx="49" cy="46" r="2.5"/><circle cx="98" cy="46" r="2.5"/><circle cx="104" cy="38" r="2.5"/>
        <circle cx="32" cy="58" r="2.5"/><circle cx="63" cy="58" r="2.5"/><circle cx="55" cy="80" r="2.5"/><circle cx="35" cy="84" r="2.5"/><circle cx="52" cy="92" r="2.5"/><circle cx="48" cy="99" r="2.5"/><circle cx="67" cy="103" r="2.5"/><circle cx="75" cy="100" r="2.5"/><circle cx="44" cy="112" r="2.5"/><circle cx="36" cy="88" r="2.5"/>
      </g>
      <g fill="var(--series-a)">
        <circle cx="106" cy="42" r="2.5"/><circle cx="120" cy="44" r="2.5"/><circle cx="128" cy="40" r="2.5"/><circle cx="109" cy="35" r="2.5"/><circle cx="162" cy="62" r="2.5"/><circle cx="172" cy="64" r="2.5"/><circle cx="144" cy="74" r="2.5"/>
        <circle cx="132" cy="82" r="2.5"/><circle cx="150" cy="88" r="2.5"/><circle cx="140" cy="92" r="2.5"/><circle cx="128" cy="98" r="2.5"/><circle cx="138" cy="103" r="2.5"/><circle cx="148" cy="100" r="2.5"/><circle cx="158" cy="96" r="2.5"/><circle cx="178" cy="98" r="2.5"/>
        <circle cx="130" cy="110" r="2.5"/><circle cx="136" cy="114" r="2.5"/><circle cx="144" cy="110" r="2.5"/><circle cx="152" cy="116" r="2.5"/><circle cx="160" cy="108" r="2.5"/><circle cx="128" cy="120" r="2.5"/><circle cx="140" cy="122" r="2.5"/><circle cx="148" cy="126" r="2.5"/><circle cx="134" cy="128" r="2.5"/>
        <circle cx="126" cy="134" r="2.5"/><circle cx="138" cy="136" r="2.5"/><circle cx="156" cy="130" r="2.5"/><circle cx="128" cy="141" r="2.5"/><circle cx="144" cy="140" r="2.5"/><circle cx="160" cy="145" r="2.5"/><circle cx="134" cy="146" r="2.5"/><circle cx="176" cy="135" r="2.5"/>
        <circle cx="218" cy="85" r="2.5"/><circle cx="222" cy="94" r="2.5"/><circle cx="200" cy="104" r="2.5"/><circle cx="212" cy="108" r="2.5"/><circle cx="220" cy="114" r="2.5"/><circle cx="230" cy="116" r="2.5"/><circle cx="204" cy="132" r="2.5"/>
      </g>
      <rect x="479" y="10" width="46" height="42" fill="#fff" stroke="#eef0f5"/>
      <text x="502" y="20" font-size="5.5" font-weight="700" text-anchor="middle">Title</text>
      <circle cx="490" cy="31" r="2.5" fill="var(--series-a)"/><text x="498" y="33" font-size="4.5">Item 1</text>
      <circle cx="490" cy="43" r="2.5" fill="var(--series-b)"/><text x="498" y="45" font-size="4.5">Item 2</text>
    </svg>
  </div>

  <aside class="abs side" style="top:20px">
    <div class="card" style="position:relative;height:182px">
      <div class="card-head">PROFILE <svg width="9" height="10" viewBox="0 0 9 10" fill="#a9b0c8"><path d="M4.5 0a3 3 0 0 1 3 3v3l1.5 2H0l1.5-2V3a3 3 0 0 1 3-3zM3.3 9h2.4a1.2 1.2 0 0 1-2.4 0z"/></svg></div>
      <div class="avatar" role="img" aria-label="Profile portrait photo"></div>
      <div class="name">Rowan Pike</div>
      <div class="email">rowanpike@ledgerworks.example</div>
    </div>
    <div class="card" style="margin-top:18px;height:87px">
      <div class="card-head">TODAYS VOLUME <span class="dots"><i></i><i></i><i></i></span></div>
      <div class="volume"><span class="plus"></span>$1840.95 (10.64%)</div>
    </div>
    <div class="card" style="position:relative;margin-top:18px;height:195px">
      <div class="card-head">CARD TITLE <span class="dots"><i></i><i></i><i></i></span></div>
      <svg class="abs" style="left:25px;top:52px" width="100" height="100" viewBox="0 0 100 100">
        <circle cx="50" cy="50" r="44" fill="none" stroke="var(--teal)" stroke-width="13" stroke-dasharray="31 246" transform="rotate(-122 50 50)"/>
        <circle cx="50" cy="50" r="44" fill="none" stroke="var(--purple)" stroke-width="13" stroke-dasharray="81 196" transform="rotate(-70 50 50)"/>
        <circle cx="50" cy="50" r="44" fill="none" stroke="var(--brand)" stroke-width="13" stroke-dasharray="131 146" transform="rotate(42 50 50)"/>
        <text x="51" y="51" text-anchor="middle" font-family="Roboto,sans-serif" font-size="13" font-weight="500" fill="#2a2d3a">23%</text>
        <text x="50" y="62" text-anchor="middle" font-family="Roboto,sans-serif" font-size="8" font-weight="500" fill="#2a2d3a">item 3</text>
      </svg>
      <div class="legend"><span><i style="background:var(--brand)"></i>Item 1</span><span><i style="background:var(--purple)"></i>Item 2</span><span><i style="background:var(--teal)"></i>Item 3</span></div>
    </div>
    <div class="cta" style="margin-top:17px">SOME BUTTON <svg width="12" height="10" viewBox="0 0 12 10" fill="none" stroke="#fff" stroke-width="1.3"><path d="M0 5h11M7 1l4 4-4 4"/></svg></div>
    <div class="actions" style="margin-top:14px">Actions
      <span class="btn" style="margin-left:22px"><svg viewBox="0 0 12 12"><path d="M1 11l.6-3L8.5 1.1l2.4 2.4L4 10.4z"/></svg></span>
      <span class="btn"><svg viewBox="0 0 12 12"><rect x="2.5" y="3" width="7" height="8.5" rx="1"/><rect x="1.5" y="1.3" width="9" height="1.2"/></svg></span>
      <span class="btn"><svg viewBox="0 0 12 12"><circle cx="2.5" cy="6" r="1.6"/><circle cx="9.5" cy="2.5" r="1.6"/><circle cx="9.5" cy="9.5" r="1.6"/><path d="M2.5 6 9.5 2.5M2.5 6l7 3.5" stroke="#a9b0c8" stroke-width="1"/></svg></span>
    </div>
  </aside>
</section>

</body>
</html>
```